Steadfast Retail Sparkfield Summit

Looking for creative, eye-catching banner ads to promote our upcoming conference in September for ecommerce merchants. See description at http://www.steadfastretail-example.com/kindle

See logos and existing banners (which we don't care for) at: http://www.steadfastretail-example.com/kindle-media

```html
<!DOCTYPE html>
<html lang="en">
<head>
<meta charset="utf-8">
<title>Steadfast Retail Sparkfield Summit – Banner Set</title>
<link href="https://fonts.googleapis.com/css2?family=Arimo:wght@400;700&display=swap" rel="stylesheet">
<style>
  :root {
    --page: #ffffff;
    --panel: #e9edf1;
    --ink: #1f2a36;
    --headline: #0f5f8c;
    --orange: #f26a24;
    --orange-light: #ff9a52;
    --orange-dark: #d4501a;
    --sky: #47b3e6;
    --sky-deep: #1e86c4;
    --knob: #7a2a0e;
    --badge: #c7cdd6;
    --photo-light: #b7c2cc;
    --photo-dark: #5d6b78;
    --frame: #9aa3ad;
  }
  html, body {
    margin: 0;
    padding: 0;
    width: 1200px;
    height: 1200px;
    overflow: hidden;
    background: var(--page);
    font-family: "Arimo", Arial, sans-serif;
  }
  .stage { position: relative; width: 1200px; height: 1200px; overflow: hidden; }
  .board {
    position: absolute; left: 0; top: 0;
    width: 850px; height: 850px;
    transform: scale(1.41176);
    transform-origin: 0 0;
  }
  .banner { position: absolute; display: block; outline: 1px solid var(--frame); }
  .banner--leaderboard { left: 69px; top: 55px; width: 728px; height: 90px; }
  .banner--rectangle { left: 69px; top: 291px; width: 300px; height: 250px; }
  .banner--skyscraper { left: 635px; top: 209px; width: 160px; height: 600px; }
  .size-label {
    position: absolute; margin: 0;
    font-size: 15px; color: var(--ink);
    transform: translateX(-50%);
    letter-spacing: 0.3px;
  }
  .size-label--leaderboard { left: 432px; top: 152px; }
  .size-label--rectangle { left: 219px; top: 556px; }
  .size-label--skyscraper { left: 715px; top: 816px; }
  svg text { font-family: "Arimo", Arial, sans-serif; }
  .wordmark { font-weight: 700; fill: var(--ink); letter-spacing: 0.3px; }
  .headline { font-weight: 700; fill: var(--headline); }
  .event-date { font-weight: 700; fill: var(--ink); }
  .cta-label { font-weight: 700; fill: #ffffff; letter-spacing: 0.3px; }
</style>
</head>
<body>
<div class="stage">
  <div class="board">

    <!-- Leaderboard 728 x 90 -->
    <svg class="banner banner--leaderboard" viewBox="0 0 728 90" aria-label="Sparkfield 2015 leaderboard banner">
      <defs>
        <linearGradient id="photoTone" x1="0" y1="0" x2="1" y2="1">
          <stop offset="0" stop-color="var(--photo-light)"/>
          <stop offset="1" stop-color="var(--photo-dark)"/>
        </linearGradient>
        <linearGradient id="ctaFill" x1="0" y1="0" x2="0" y2="1">
          <stop offset="0" stop-color="var(--orange-light)"/>
          <stop offset="1" stop-color="var(--orange-dark)"/>
        </linearGradient>
        <linearGradient id="skyBand" x1="0" y1="0" x2="1" y2="0">
          <stop offset="0" stop-color="var(--sky-deep)"/>
          <stop offset="1" stop-color="var(--sky)"/>
        </linearGradient>
      </defs>
      <rect class="panel" width="728" height="90" fill="var(--panel)"/>
      <g role="img" aria-label="Photo of two business people in front of office towers">
        <polygon points="418,0 728,0 728,90 396,90" fill="url(#photoTone)"/>
      </g>
      <polygon class="accent-slash" points="404,90 426,0 440,0 418,90" fill="var(--orange)"/>
      <polygon class="accent-corner" points="620,0 660,0 600,40" fill="var(--orange)"/>
      <rect class="sky-band" x="560" y="46" width="168" height="44" fill="url(#skyBand)"/>
      <polygon class="brand-zone" points="0,0 168,0 176,45 168,90 0,90" fill="#ffffff"/>
      <polygon class="chevron" points="168,0 180,0 188,45 180,90 168,90 176,45" fill="#111111"/>
      <text class="wordmark" x="84" y="49" font-size="16" text-anchor="middle">SPARKFIELD 2015</text>
      <text class="event-date" x="84" y="70" font-size="13" text-anchor="middle">September 16 - 17</text>
      <text class="headline" x="190" y="23" font-size="21">The Event For</text>
      <text class="headline" x="190" y="46" font-size="21">Ecommerce</text>
      <text class="headline" x="190" y="69" font-size="21">Enterpreneurs</text>
      <path class="swoosh" d="M200 84 Q270 72 360 74" stroke="var(--orange)" stroke-width="3" fill="none" stroke-linecap="round"/>
      <ellipse class="guarantee-seal" cx="364" cy="33" rx="28" ry="13" fill="var(--badge)"/>
      <g class="cta">
        <rect x="590" y="40" width="128" height="36" rx="3" fill="url(#ctaFill)"/>
        <text class="cta-label" x="636" y="63" font-size="14" text-anchor="middle">REGISTER</text>
        <circle cx="699" cy="58" r="11" fill="var(--knob)" stroke="#ffffff" stroke-width="2"/>
        <polygon points="695,52 705,58 695,64" fill="var(--orange-light)"/>
      </g>
    </svg>
    <p class="size-label size-label--leaderboard">728X90</p>

    <!-- Medium rectangle 300 x 250 -->
    <svg class="banner banner--rectangle" viewBox="0 0 300 250" aria-label="Sparkfield 2015 medium rectangle banner">
      <rect class="panel" width="300" height="250" fill="var(--panel)"/>
      <g role="img" aria-label="Photo of two business people in front of office towers">
        <polygon points="188,50 300,46 300,250 198,250 172,150" fill="url(#photoTone)"/>
      </g>
      <polygon class="accent-chevron" points="190,52 200,52 176,150 206,250 194,250 164,150" fill="var(--orange)"/>
      <rect class="brand-zone" width="300" height="40" fill="#ffffff"/>
      <path class="header-swoosh" d="M0 38 Q150 28 300 40 L300 50 Q150 38 0 54 Z" fill="#111111"/>
      <text class="wordmark" x="150" y="27" font-size="18" text-anchor="middle">SPARKFIELD 2015</text>
      <text class="headline" x="76" y="83" font-size="28" text-anchor="middle">The Event</text>
      <text class="headline" x="76" y="101" font-size="18" text-anchor="middle">For</text>
      <text class="headline" x="76" y="120" font-size="20" text-anchor="middle">Ecommerce</text>
      <text class="headline" x="76" y="139" font-size="20" text-anchor="middle">Enterpreneurs</text>
      <path class="swoosh" d="M12 152 Q80 142 152 146" stroke="var(--orange)" stroke-width="3" fill="none" stroke-linecap="round"/>
      <ellipse class="guarantee-seal" cx="32" cy="180" rx="26" ry="12" fill="var(--badge)"/>
      <text class="event-date" x="110" y="170" font-size="13" text-anchor="middle">September</text>
      <text class="event-date" x="110" y="186" font-size="13" text-anchor="middle">16 - 17</text>
      <polygon class="sky-band" points="0,198 172,198 188,250 0,250" fill="url(#skyBand)"/>
      <g class="cta">
        <rect x="27" y="206" width="128" height="36" rx="3" fill="url(#ctaFill)"/>
        <text class="cta-label" x="73" y="229" font-size="14" text-anchor="middle">REGISTER</text>
        <circle cx="137" cy="224" r="11" fill="var(--knob)" stroke="#ffffff" stroke-width="2"/>
        <polygon points="133,218 143,224 133,230" fill="var(--orange-light)"/>
      </g>
    </svg>
    <p class="size-label size-label--rectangle">300X250</p>

    <!-- Skyscraper 160 x 600 -->
    <svg class="banner banner--skyscraper" viewBox="0 0 160 600" aria-label="Sparkfield 2015 skyscraper banner">
      <rect class="panel" width="160" height="600" fill="var(--panel)"/>
      <g role="img" aria-label="Photo of two business people in front of office towers">
        <polygon points="0,330 160,272 160,540 0,540" fill="url(#photoTone)"/>
      </g>
      <polygon class="accent-top" points="0,328 160,268 160,284 14,344 0,352" fill="var(--orange)"/>
      <polygon class="accent-bottom" points="0,505 0,540 20,540" fill="var(--orange)"/>
      <polygon class="accent-bottom" points="120,540 160,520 160,540" fill="var(--orange)"/>
      <polygon class="brand-zone" points="0,0 160,0 160,56 80,72 0,56" fill="#ffffff"/>
      <polygon class="chevron" points="0,54 80,70 160,54 160,62 80,80 0,62" fill="#111111"/>
      <text class="wordmark" x="80" y="33" font-size="14" text-anchor="middle">SPARKFIELD 2015</text>
      <text class="headline" x="80" y="121" font-size="26" text-anchor="middle">The</text>
      <text class="headline" x="80" y="146" font-size="26" text-anchor="middle">Event</text>
      <text class="headline" x="80" y="170" font-size="18" text-anchor="middle">For</text>
      <text class="headline" x="80" y="194" font-size="20" text-anchor="middle">Ecommerce</text>
      <text class="headline" x="80" y="218" font-size="20" text-anchor="middle">Enterpreneurs</text>
      <path class="swoosh" d="M16 232 Q80 222 150 226" stroke="var(--orange)" stroke-width="3" fill="none" stroke-linecap="round"/>
      <text class="event-date" x="80" y="254" font-size="13" text-anchor="middle">September 16 - 17</text>
      <ellipse class="guarantee-seal" cx="40" cy="285" rx="30" ry="13" fill="var(--badge)"/>
      <rect class="sky-band" x="0" y="536" width="160" height="64" fill="url(#skyBand)"/>
      <g class="cta">
        <rect x="10" y="548" width="140" height="38" rx="3" fill="url(#ctaFill)"/>
        <text class="cta-label" x="62" y="572" font-size="15" text-anchor="middle">REGISTER</text>
        <circle cx="130" cy="567" r="12" fill="var(--knob)" stroke="#ffffff" stroke-width="2"/>
        <polygon points="126,561 136,567 126,573" fill="var(--orange-light)"/>
      </g>
    </svg>
    <p class="size-label size-label--skyscraper">160X600</p>

  </div>
</div>
</body>
</html>
```